The Farrowdale Penick Firm

We are a real estate and business acquisition services company that provides consulting services to large companies and individuals. The company provided nationwide services to companies looking to expand through opening new locations or buying other companies in their field. We work very close with attorneys, accountants, banks/financial institutions and high level executives and business owners.

Target Market(s)

CEO, VP, business owners and bankers.

Industry/Entity Type

Real Estate

Requirements
Must have
• I am looking for a design that looks very professional and has a classic, trustworthy, professional feeling. I want the letterhead and return address to look formal and official so this it is not tossed out as junk mail. FP or FPF can be used in a logo style part but that is not required. Our tag line is "Real Estate and Business Acquisition Services". This should be on the letter head but not on the return address. It does not need a lot of color but I will leave that to your tasteful choice. It should be rich and formal looking.
Should not have
• I do not want anything that looks like a cartoon drawing or figure. Use font that gives a strong trustworthy look. We are not a law firm so no scales or gavels. A law firm sort of look or feel is OK.

```html
<!DOCTYPE html>
<html lang="en">
<head>
<meta charset="utf-8">
<title>The Farrowdale Penick Firm – Letterhead</title>
<link rel="stylesheet" href="https://fonts.googleapis.com/css2?family=Bodoni+Moda:ital,opsz,wght@0,6..96,500;0,6..96,600;1,6..96,500&display=swap">
<style>
  :root {
    --navy: #1f3a7a;
    --lime: #cfdc45;
    --paper: #ffffff;
  }
  html, body {
    margin: 0;
    padding: 0;
    overflow: hidden;
    background: var(--paper);
  }
  .letterhead {
    position: relative;
    width: 1200px;
    height: 450px;
    background: var(--paper);
    color: var(--navy);
    font-family: "Bodoni Moda", "Didot", serif;
    overflow: hidden;
  }
  .brand-mark {
    position: absolute;
    left: 58px;
    top: 100px;
    width: 88px;
    height: 88px;
    background: var(--lime);
  }
  .spine-rule {
    position: absolute;
    left: 167px;
    top: 47px;
    width: 7px;
    height: 326px;
    background: var(--lime);
  }
  .firm-name {
    position: absolute;
    left: 187px;
    top: 52px;
    margin: 0;
    font-size: 45px;
    font-weight: 500;
    line-height: 1;
    letter-spacing: 0;
    white-space: nowrap;
  }
  .header-rule {
    position: absolute;
    left: 185px;
    top: 156px;
    width: 672px;
    height: 4px;
    background: var(--lime);
  }
  .tagline {
    position: absolute;
    left: 190px;
    top: 192px;
    margin: 0;
    font-size: 28px;
    font-style: italic;
    font-weight: 500;
    line-height: 1;
    white-space: nowrap;
  }
  .contact-line {
    position: absolute;
    left: 188px;
    margin: 0;
    font-weight: 600;
    line-height: 1;
    white-space: nowrap;
    display: flex;
    align-items: center;
  }
  .contact-line--address { top: 296px; font-size: 22px; }
  .contact-line--phone { top: 342px; font-size: 20px; }
  .divider {
    display: inline-block;
    width: 2px;
    height: 1.4em;
    background: var(--lime);
    margin: 0 20px;
  }
</style>
</head>
<body>
  <div class="letterhead">
    <div class="brand-mark" aria-hidden="true"></div>
    <div class="spine-rule" aria-hidden="true"></div>

    <h1 class="firm-name">The Farrowdale Penick Firm</h1>
    <div class="header-rule" aria-hidden="true"></div>
    <p class="tagline">Real Estate &amp; Business Acquisition Services</p>

    <p class="contact-line contact-line--address">
      <span>2718 Alder Creek Road, Suite 560</span>
      <span class="divider" aria-hidden="true"></span>
      <span>Riverton, KY</span>
      <span class="divider" aria-hidden="true"></span>
      <span>40999</span>
    </p>
    <p class="contact-line contact-line--phone">
      <span>phone : 615.555.0142</span>
      <span class="divider" aria-hidden="true"></span>
      <span>www.farrowdalepenick.com</span>
    </p>
  </div>
</body>
</html>
```